Business card design for a real estate company

We need a business card design a real estate development company called "Quindaro Holding SA" in Switzerland. Space needed for two phone numbers in international format (one is +7 (912) xxx-xx-xx, the other +41 (76) xxx-xx-xx), e-mail (ml@quindaro-example.com), name, position and address of the company:
Rue des Tilleuls 24
CH-1700 Fribourg
Switzerland

Target Market(s)

Potential partners, architects, banks etc..

Industry/Entity Type

Business

Requirements
Must have
• Slight, elegant.
Should not have
• Do not include illustrations of buildings etc..

```html
<!DOCTYPE html>
<html lang="en">
<head>
<meta charset="utf-8">
<title>Quindaro Holding SA — Business Card</title>
<link rel="stylesheet" href="https://fonts.googleapis.com/css2?family=Montserrat:wght@400;500&family=Arimo:wght@500&display=swap">
<style>
  :root {
    --card-bg: #ffffff;
    --ink-grey: #6c6c6c;
    --ink-mark: #8c8c8c;
    --ink-dark: #111111;
  }
  html, body {
    margin: 0;
    padding: 0;
    width: 1200px;
    height: 777px;
    overflow: hidden;
    background: var(--card-bg);
  }
  .card {
    position: relative;
    width: 1200px;
    height: 777px;
    background: var(--card-bg);
    font-family: "Montserrat", sans-serif;
    font-variant: small-caps;
  }
  .card > * {
    position: absolute;
    margin: 0;
    line-height: 1;
    white-space: nowrap;
  }
  .company-name {
    left: 296px;
    top: 196px;
    font-size: 44px;
    font-weight: 400;
    letter-spacing: 0.13em;
    color: var(--ink-grey);
  }
  .brand-mark {
    left: 40px;
    top: 322px;
    font-size: 38px;
    font-weight: 400;
    letter-spacing: 0.04em;
    font-variant: normal;
    color: var(--ink-mark);
  }
  .person-name {
    left: 296px;
    top: 423px;
    font-size: 28px;
    font-weight: 500;
    letter-spacing: 0.14em;
    color: var(--ink-dark);
  }
  .person-role {
    left: 296px;
    top: 465px;
    font-size: 28px;
    font-weight: 400;
    letter-spacing: 0.14em;
    color: var(--ink-grey);
  }
  .address,
  .contacts {
    top: 570px;
    font-size: 28px;
    letter-spacing: 0.12em;
    color: var(--ink-grey);
  }
  .address { left: 296px; }
  .contacts { left: 793px; }
  .address span,
  .contacts span {
    display: block;
    height: 42px;
  }
  .contacts .phone {
    font-variant: normal;
    letter-spacing: 0.08em;
  }
  .contacts .email {
    font-family: "Arimo", sans-serif;
    font-weight: 500;
    font-variant: normal;
    letter-spacing: 0.01em;
    font-size: 29px;
    color: var(--ink-dark);
  }
</style>
</head>
<body>
  <main class="card">
    <h1 class="company-name">Quindaro Holding SA</h1>
    <div class="brand-mark">Quindaro</div>

    <p class="person-name">Marc Lemaire</p>
    <p class="person-role">Director</p>

    <address class="address" style="font-style: normal;">
      <span>Rue des Tilleuls 24</span>
      <span>CH-1700 Fribourg</span>
      <span>Switzerland</span>
    </address>

    <div class="contacts">
      <span class="phone">+7 (912) xxx-xx-xx</span>
      <span class="phone">+41 (76) xxx-xx-xx</span>
      <span class="email">ml@quindaro-example.com</span>
    </div>
  </main>
</body>
</html>
```